Canvasline Registry, LLC needs clean, modern business card design

Canvasline Registry is based in Honolulu. We offer fine arts collections management and documentation services for private and corporate art collectors. I would like to use my logo (attached). Card can be either single or double sided and either vertical or horizontal. My clients are businesses with art collections (banks, law firms, etc.) and wealthy individual collectors.

```html
<!DOCTYPE html>
<html lang="en">
<head>
<meta charset="utf-8">
<title>Canvasline Registry – Business Card</title>
<link rel="stylesheet" href="https://fonts.googleapis.com/css2?family=Roboto:wght@300;400;500&display=swap">
<style>
  :root {
    --backdrop: #e6e4e0;
    --card: #ffffff;
    --ink: #222222;
    --ink-soft: #4a4a4a;
    --band: #6b6b6b;
    --band-text: #ffffff;
    --accent: #2a9fd8;
    --ornament: rgba(190, 222, 224, 0.55);
    --ornament-fade: rgba(190, 222, 224, 0);
    --sketch: rgba(200, 200, 200, 0.55);
    --sketch-fade: rgba(200, 200, 200, 0);
  }
  * { box-sizing: border-box; margin: 0; padding: 0; }
  html, body {
    width: 1200px; height: 1200px; overflow: hidden;
    background: var(--backdrop);
    font-family: "Roboto", Arial, sans-serif;
  }
  .card {
    position: absolute; left: 300px; top: 75px;
    width: 600px; height: 1050px;
    background: var(--card);
    border-radius: 14px;
    box-shadow: 0 10px 30px rgba(0,0,0,.18);
    overflow: hidden;
  }
  .ornament-top, .ornament-bottom, .portrait-sketch { position: absolute; }
  .ornament-top {
    left: -60px; top: -80px; width: 720px; height: 420px;
    border-radius: 50%;
    background: radial-gradient(ellipse at 55% 45%, var(--ornament) 0%, var(--ornament-fade) 70%);
  }
  .ornament-bottom {
    left: -80px; top: 600px; width: 440px; height: 380px;
    border-radius: 50%;
    background: radial-gradient(ellipse at 45% 45%, var(--ornament) 0%, var(--ornament-fade) 70%);
  }
  .portrait-sketch {
    right: 10px; top: 640px; width: 200px; height: 290px;
    border-radius: 50% 50% 40% 40%;
    background: radial-gradient(ellipse at 50% 45%, var(--sketch) 0%, var(--sketch-fade) 72%);
  }
  .brand {
    position: absolute; left: 70px; top: 330px;
    display: flex; align-items: center; gap: 18px;
  }
  .brand-mark {
    width: 64px; height: 64px; border-radius: 50%;
    background: var(--accent);
  }
  .brand-name {
    font-size: 40px; font-weight: 400; color: var(--ink); letter-spacing: .5px;
  }
  .tagline {
    position: absolute; left: 70px; top: 420px;
    font-size: 19px; color: var(--ink); letter-spacing: .6px;
  }
  .role {
    position: absolute; right: 50px; top: 462px;
    font-size: 24px; font-weight: 300; color: var(--ink-soft);
  }
  .name-band {
    position: absolute; left: 0; top: 496px; width: 600px; height: 74px;
    background: var(--band);
    display: flex; align-items: center; padding-left: 70px;
  }
  .name {
    font-size: 42px; font-weight: 300; color: var(--band-text); letter-spacing: 1px;
  }
  .address {
    position: absolute; left: 70px; top: 600px;
    font-size: 17px; color: var(--ink);
  }
  .contact {
    position: absolute; left: 40px; top: 950px;
    font-size: 28px; line-height: 1.25; color: var(--ink); letter-spacing: .5px;
  }
</style>
</head>
<body>
  <main class="card">
    <div class="ornament-top" role="img" aria-label="Soft teal peacock-feather ornament"></div>
    <div class="ornament-bottom" role="img" aria-label="Soft teal peacock-feather ornament"></div>
    <div class="portrait-sketch" role="img" aria-label="Pencil-sketch illustration of a seated figure"></div>

    <div class="brand">
      <span class="brand-mark"></span>
      <span class="brand-name">Canvasline Registry</span>
    </div>
    <p class="tagline">"Fine Arts Collections Management Services"</p>
    <p class="role">Manager</p>
    <div class="name-band"><h1 class="name">Marla J. Whitcombe</h1></div>
    <p class="address">1420 Kapena Lane Honolulu, HI 96822 (808) 555-0147</p>
    <p class="contact">hello@canvaslinereg.com<br>www.canvaslinereg.com</p>
  </main>
</body>
</html>
```